Business Card Design with a glossy effect please

We supply and install Glass pool fencing: in Frameless, Semi Frameless, and Stainless Steel we also install Glass Balustrading, interior and exterior, plus Aluminium Tubular and Gates and Screens, and Vitra KP4482 Glass protection

Dale Purvis
M 0438516290 or T 08 9517 3364
Unit 3 / 41 Kestrel Parade, Marlow Bay 6072
ABN: 51804127739
www.tidewell-poolbarriers.com.au
info@tidewell-poolbarriers.com.au

```html
<!DOCTYPE html>
<html lang="en">
<head>
<meta charset="utf-8">
<title>Tidewell Pool Barriers – Business Card</title>
<link rel="stylesheet" href="https://fonts.googleapis.com/css2?family=Open+Sans:ital,wght@0,400;0,600;1,400&display=swap">
<style>
  :root {
    --bg: #b9b9b9;
    --sky: #29a9e0;
    --sky-mid: #1e9bd7;
    --sky-deep: #0f76bf;
    --navy: #0d4a6e;
    --navy-band: #0a4468;
    --rule: #2aa3dc;
    --ink: #1f1f1f;
    --white: #ffffff;
  }
  * { box-sizing: border-box; margin: 0; padding: 0; }
  html, body { width: 1200px; height: 660px; overflow: hidden; }
  body {
    background: var(--bg);
    font-family: "Open Sans", Arial, sans-serif;
    position: relative;
  }
  .card {
    position: absolute;
    top: 160px;
    width: 528px;
    height: 317px;
    overflow: hidden;
  }
  /* Front */
  .card--front { left: 60px; background: var(--sky); }
  .card--front .band { position: absolute; top: 0; bottom: 0; }
  .band--mid { left: 290px; width: 136px; background: var(--sky-mid); }
  .band--deep { left: 426px; right: 0; background: var(--sky-deep); }
  .front-name {
    position: absolute;
    left: 30px;
    top: 130px;
    color: var(--white);
    font-weight: 600;
    line-height: 1;
  }
  .front-name .word-main { display: block; font-size: 42px; letter-spacing: 1.5px; }
  .front-name .word-sub { display: block; font-size: 15px; letter-spacing: 3.2px; margin-top: 4px; padding-left: 2px; }

  /* Back */
  .card--back { left: 630px; background: var(--white); }
  .brand {
    position: absolute;
    left: 26px;
    top: 24px;
    display: flex;
    align-items: center;
    gap: 18px;
    color: var(--navy);
    font-weight: 600;
  }
  .brand-square { width: 56px; height: 56px; background: var(--sky); flex: none; }
  .brand-name { line-height: 1; }
  .brand-name .word-main { display: block; font-size: 46px; letter-spacing: 2px; }
  .brand-name .word-sub { display: block; font-size: 16px; letter-spacing: 4px; margin-top: 3px; padding-left: 2px; }

  .person { position: absolute; left: 22px; top: 128px; }
  .person-name { font-size: 22px; font-weight: 600; color: var(--navy); letter-spacing: 1.5px; line-height: 1; }
  .person-role { font-size: 14px; color: var(--ink); margin-top: 8px; }
  .abn { position: absolute; left: 198px; top: 165px; font-size: 13px; font-style: italic; color: var(--ink); }
  .divider { position: absolute; left: 0; top: 186px; width: 310px; height: 2px; background: var(--rule); }

  .contacts { position: absolute; left: 20px; top: 199px; list-style: none; }
  .contacts li { display: flex; align-items: center; gap: 8px; height: 19px; font-size: 13px; color: var(--ink); }
  .contacts svg { width: 11px; height: 11px; flex: none; }

  .decor { position: absolute; left: 0; top: 0; width: 528px; height: 317px; }
  .address {
    position: absolute;
    left: 20px;
    top: 293px;
    font-size: 12.5px;
    font-weight: 600;
    color: var(--white);
    white-space: nowrap;
  }
</style>
</head>
<body>

<section class="card card--front" aria-label="Card front">
  <div class="band band--mid"></div>
  <div class="band band--deep"></div>
  <div class="front-name">
    <span class="word-main">TIDEWELL</span>
    <span class="word-sub">POOL BARRIERS</span>
  </div>
</section>

<section class="card card--back" aria-label="Card back">
  <svg class="decor" viewBox="0 0 528 317" aria-hidden="true">
    <defs>
      <linearGradient id="glassTone" x1="0" y1="0" x2="1" y2="0">
        <stop offset="0" stop-color="#3cb4e6"/>
        <stop offset="1" stop-color="#1d98d6"/>
      </linearGradient>
    </defs>
    <polygon points="318,185 528,138 528,317 318,317" fill="url(#glassTone)"/>
    <polygon points="0,282 270,282 412,317 0,317" fill="var(--navy-band)"/>
    <polygon points="270,282 282,282 424,317 412,317" fill="var(--white)"/>
  </svg>

  <div class="brand">
    <div class="brand-square"></div>
    <div class="brand-name">
      <span class="word-main">TIDEWELL</span>
      <span class="word-sub">POOL BARRIERS</span>
    </div>
  </div>

  <div class="person">
    <div class="person-name">DALE PURVIS</div>
    <div class="person-role">Director</div>
  </div>
  <div class="abn">ABN: 51804127739</div>
  <div class="divider"></div>

  <ul class="contacts">
    <li>
      <svg viewBox="0 0 11 11"><rect width="11" height="11" rx="1.5" fill="var(--navy)"/><rect x="3.5" y="1.8" width="4" height="7.4" rx="0.8" fill="none" stroke="#fff" stroke-width="1"/></svg>
      0438516290
    </li>
    <li>
      <svg viewBox="0 0 11 11"><rect width="11" height="11" rx="1.5" fill="var(--navy)"/><path d="M3 2.2 L4.6 3.8 L3.9 4.8 Q4.8 6.4 6.2 7.1 L7.2 6.4 L8.8 8 L7.8 9 Q4.6 8.6 2 4 Z" fill="#fff"/></svg>
      08 9517 3364
    </li>
    <li>
      <svg viewBox="0 0 11 11"><rect width="11" height="11" rx="1.5" fill="var(--navy)"/><rect x="2" y="3" width="7" height="5" fill="none" stroke="#fff" stroke-width="0.9"/><path d="M2 3 L5.5 6 L9 3" fill="none" stroke="#fff" stroke-width="0.9"/></svg>
      www.tidewell-poolbarriers.com.au
    </li>
    <li>
      <svg viewBox="0 0 11 11"><rect width="11" height="11" rx="1.5" fill="var(--navy)"/><circle cx="5.5" cy="5.5" r="3.5" fill="none" stroke="#fff" stroke-width="0.8"/><ellipse cx="5.5" cy="5.5" rx="1.5" ry="3.5" fill="none" stroke="#fff" stroke-width="0.7"/><line x1="2" y1="5.5" x2="9" y2="5.5" stroke="#fff" stroke-width="0.7"/></svg>
      info@tidewell-poolbarriers.com.au
    </li>
  </ul>

  <div class="address">UNIT 3 / 41 KESTREL PARADE, MARLOW BAY 6072</div>
</section>

</body>
</html>
```